Business Card Design

Tumble Bay is a Laundromat Store
we provide wash and Fold service to Customers who are busy with their life and can not come to the store and do laundry
we have customers who drop their laundry at the store
but now i want to provide service to customers who are not able to come to the store to drop. i will go to their address and pickup the laundry and get it washed folded and delivered
Updates
Can you use the colour in you design which i uploaded and also fusha fluorescent green bright pink
Target Market(s)
all works of life who don't have time to do laundry
Industry/Entity Type
Store
Contact Information for Business Card
TumbleBay Laundromat
247 Orchard Lane
Lynn MA 01958
Look and feel
Each slider illustrates characteristics of the customer's brand and the style your logo design should communicate.

```html
<!DOCTYPE html>
<html lang="en">
<head>
<meta charset="UTF-8">
<title>TumbleBay Laundromat – Business Card</title>
<link href="https://fonts.googleapis.com/css2?family=Lato:wght@400;700;900&display=swap" rel="stylesheet">
<style>
  :root {
    --stage: #2d2d2f;
    --card-dark: #120c14;
    --card-glow: #3a1d3a;
    --pink: #ec1a8c;
    --pink-deep: #d5107c;
    --blue: #1f5fb8;
    --white: #ffffff;
    --laundry-mixed: #c9a4b8;
    --laundry-folded: #8a6c8e;
    --icon-fill: #e9e4ea;
  }
  * { box-sizing: border-box; margin: 0; padding: 0; }
  html, body {
    width: 1200px; height: 900px; overflow: hidden;
    background: var(--stage);
    font-family: "Lato", Arial, sans-serif;
  }
  .stage {
    width: 1200px; height: 900px;
    display: flex; align-items: center; justify-content: center;
  }
  .card {
    position: relative;
    width: 1050px; height: 600px;
    overflow: hidden;
    background: radial-gradient(ellipse at 50% 35%, var(--card-glow) 0%, var(--card-dark) 70%);
    color: var(--white);
    box-shadow: 0 20px 50px rgba(0,0,0,.55);
  }
  .brand {
    position: absolute; top: 48px; left: 0; width: 100%;
    text-align: center;
    font-size: 48px; font-weight: 400; letter-spacing: .5px;
    color: var(--white);
  }
  .brand-dot {
    display: inline-block; width: 16px; height: 16px;
    border-radius: 50%; background: var(--pink);
    margin-right: 14px; vertical-align: middle;
  }
  .address {
    position: absolute; top: 118px; left: 0; width: 100%;
    text-align: center;
    font-size: 26px; font-weight: 700; letter-spacing: 4px;
    text-transform: uppercase;
  }
  .call {
    position: absolute; top: 170px; left: 50%; transform: translateX(-50%);
    background: var(--pink);
    padding: 6px 18px;
    font-size: 26px; font-weight: 700; white-space: nowrap;
  }
  .laundry {
    position: absolute; border-radius: 40% 40% 10% 10%;
  }
  .laundry-dirty {
    left: 260px; top: 230px; width: 250px; height: 180px;
    background: radial-gradient(ellipse at 50% 55%, var(--laundry-mixed), #6d5a6c 85%);
  }
  .laundry-clean {
    left: 600px; top: 212px; width: 200px; height: 190px;
    border-radius: 8px;
    background: linear-gradient(180deg, #b7a6c2 0%, var(--laundry-folded) 40%, #6e4d5c 70%, #9c3b48 100%);
  }
  .band { position: absolute; left: 0; top: 0; }
  .transform-badge {
    position: absolute; left: 450px; top: 230px;
    width: 150px; height: 150px; border-radius: 50%;
    background: var(--blue);
    border: 3px solid var(--white);
  }
  .transform-badge span {
    position: absolute; left: 0; width: 100%; text-align: center;
    font-size: 28px; font-weight: 700;
  }
  .transform-badge .from { top: 26px; }
  .transform-badge .to { top: 88px; left: -12px; }
  .transform-badge svg { position: absolute; left: 0; top: 0; }
  .step-icon {
    position: absolute; width: 104px; height: 104px; border-radius: 50%;
    background: var(--white);
    display: flex; align-items: center; justify-content: center;
  }
  .step-icon i {
    display: block; width: 72px; height: 72px; border-radius: 50%;
    background: var(--icon-fill);
  }
  .step-caption {
    position: absolute; width: 240px; text-align: center;
    font-size: 20px; font-weight: 700; line-height: 1.25;
  }
</style>
</head>
<body>
<main class="stage">
  <article class="card">
    <h1 class="brand"><span class="brand-dot"></span>TumbleBay Laundromat</h1>
    <p class="address">247 Orchard Lane Lynn MA 01958</p>
    <p class="call">CALL US: +1 (781) 555-0147</p>

    <div class="laundry laundry-dirty" role="img" aria-label="Pile of crumpled dirty laundry"></div>
    <div class="laundry laundry-clean" role="img" aria-label="Stack of neatly folded clean clothes"></div>

    <div class="transform-badge">
      <span class="from">FROM</span>
      <span class="to">TO</span>
      <svg width="150" height="150" viewBox="0 0 150 150" aria-hidden="true">
        <g stroke="#fff" stroke-width="2" fill="none" stroke-dasharray="4 3">
          <line x1="120" y1="75" x2="36" y2="75"/>
          <line x1="30" y1="128" x2="118" y2="128" stroke-dasharray="none" opacity="0"/>
          <line x1="62" y1="118" x2="132" y2="118"/>
        </g>
        <path d="M36 69 L26 75 L36 81 Z" fill="#fff"/>
        <path d="M130 112 L140 118 L130 124 Z" fill="#fff"/>
      </svg>
    </div>

    <svg class="band" width="1050" height="600" viewBox="0 0 1050 600" aria-hidden="true">
      <path d="M0 440 Q525 360 1050 440 L1050 600 L0 600 Z" fill="var(--pink)"/>
      <path d="M0 505 Q525 510 1050 450 L1050 600 L0 600 Z" fill="var(--blue)"/>
      <g fill="none" stroke="#fff" stroke-width="3" stroke-linecap="round">
        <path d="M225 470 Q275 440 325 462"/>
        <path d="M470 455 Q520 425 570 445"/>
        <path d="M720 440 Q770 410 820 428"/>
      </g>
      <g fill="#fff">
        <path d="M328 454 L336 466 L320 468 Z"/>
        <path d="M573 437 L581 449 L565 451 Z"/>
        <path d="M823 420 L831 432 L815 434 Z"/>
      </g>
    </svg>

    <div class="step-icon" style="left:110px; top:428px;" role="img" aria-label="Schedule calendar illustration"><i></i></div>
    <div class="step-icon" style="left:345px; top:412px;" role="img" aria-label="House illustration"><i></i></div>
    <div class="step-icon" style="left:595px; top:398px;" role="img" aria-label="Laundry delivery van illustration"><i></i></div>
    <div class="step-icon" style="left:840px; top:378px;" role="img" aria-label="Happy customer emoji illustration"><i></i></div>

    <p class="step-caption" style="left:42px; top:540px;">You Schedule<br>A Pick-Up</p>
    <p class="step-caption" style="left:277px; top:527px;">We Pick-Up<br>Your Dirty Laundry</p>
    <p class="step-caption" style="left:527px; top:510px;">We Wash, Dry, Fold<br>&amp; Return Clean Laundry</p>
    <p class="step-caption" style="left:772px; top:490px;">Enjoy Effortless<br>Clean Laundry</p>
  </article>
</main>
</body>
</html>
```